依頼詳細
留学生向けのアルバイト募集のA4チラシ(印刷後壁に貼り付け)を作成します。複数の企業が参加し、共通のテンプレートを使用し、1店舗(例:xx居酒屋 xx店)1枚で印刷します。そこでその雛形のデザインをお願いしたいと思います。
レイアウトは添付ファイルにこだわる必要はないです。
*どのような業種職種でも使える汎用性の高いデザインでお願いします。
記載項目
ロゴ(写真データ)/紹介写真(写真データ)店名/業種/給与/勤務時間/最寄駅/PR文/応募条件/応募連絡先/先輩の声/先輩の写真(写真データ)/名前/出身/年齢/日本語レベル/在日期間
また、テキスト入力の部分は名前/出身/年齢/日本語レベル/在日期間を除く全ての部分にふりがなを付けられるようにしてください。(添付ファイル参照)

写真データ以外は全てテキストデータで入力

```html
<!DOCTYPE html>
<html lang="ja">
<head>
<meta charset="utf-8">
<title>アルバイト募集 居酒屋まねき 赤坂見附店</title>
<link rel="stylesheet" href="https://fonts.googleapis.com/css2?family=Noto+Sans+JP:wght@400;500;700;900&family=Varela+Round&display=swap">
<style>
:root{
  --red:#d9262f;
  --yellow:#f6cf1a;
  --ink:#1a1a1a;
  --paper:#ffffff;
  --sky:#bfe2ee;
  --card:#e4f0f4;
  --line:#c9c9c9;
  --stripe-green:#3fae5a;
  --stripe-blue:#2f7fc1;
}
*{margin:0;padding:0;box-sizing:border-box}
html,body{width:872px;height:1200px;overflow:hidden;background:var(--paper)}
body{font-family:"Noto Sans JP",sans-serif;color:var(--ink);position:relative}
rt{font-size:9px;font-weight:400;letter-spacing:0}
.abs{position:absolute}

.side-stripe{left:0;top:0;width:14px;height:135px;display:flex;flex-direction:column}
.side-stripe span{flex:1}
.side-stripe span:nth-child(1){background:var(--red)}
.side-stripe span:nth-child(2){background:var(--yellow)}
.side-stripe span:nth-child(3){background:var(--stripe-green)}
.side-stripe span:nth-child(4){background:var(--stripe-blue)}

.hiring-banner{left:14px;top:22px;width:560px;height:86px;background:var(--red);color:#fff;
  font-family:"Varela Round",sans-serif;font-size:66px;line-height:86px;padding-left:24px}
.get-job{left:672px;top:12px;width:172px;height:108px;background:var(--yellow);border:4px solid var(--ink);
  color:var(--red);font-weight:900;font-size:40px;line-height:46px;text-align:center;padding-top:6px;font-family:"Varela Round",sans-serif}

.shop-mark{left:28px;top:135px;width:104px;height:104px;border-radius:50%;background:var(--red)}
.shop-name{left:150px;top:148px;font-size:50px;font-weight:900;line-height:1.5;white-space:nowrap}
.shop-name rt{font-size:13px;font-weight:500}
.shop-rule{left:150px;top:236px;width:694px;height:3px;background:var(--ink)}

.shop-photo{left:28px;top:255px;width:462px;height:297px;background:linear-gradient(135deg,#3b2a20,#8a6a4c 55%,#d8c7a8)}
.pr-box{left:505px;top:255px;width:340px;height:297px;border:3px solid var(--ink);padding:14px 16px;
  font-size:20px;font-weight:700;line-height:2.05}
.pr-box .accent{color:var(--red)}

.info{left:28px;top:562px;width:477px;border-collapse:collapse}
.info th{background:var(--ink);color:#fff;width:140px;font-size:17px;font-weight:700;text-align:left;padding:6px 10px;line-height:1.4;vertical-align:middle}
.info th small{display:block;font-size:11px;font-weight:400}
.info td{border:2px solid var(--ink);font-size:20px;font-weight:700;padding:4px 12px;line-height:1.9}
.qual{left:512px;top:562px;width:333px;height:210px;border-collapse:collapse}
.qual th{background:var(--ink);color:#fff;width:112px;font-size:17px;font-weight:700;text-align:left;padding:6px 10px;line-height:1.4}
.qual th small{display:block;font-size:11px;font-weight:400}
.qual td{border:2px solid var(--ink);font-size:19px;font-weight:700;padding:4px 12px;line-height:1.9}
.qual .sub{padding-left:18px}

.call{left:28px;top:782px;width:477px;height:88px;background:var(--sky);padding:6px 16px}
.call-head{display:flex;align-items:center;gap:10px;font-family:"Varela Round",sans-serif;font-size:20px;color:var(--red)}
.call-number{font-size:44px;font-weight:900;line-height:52px;letter-spacing:1px}
.company{left:512px;top:782px;width:333px;height:88px;font-size:17px;font-weight:700;line-height:1.95;padding:2px 4px}

.voice{top:882px;width:400px;height:304px;background:var(--card);padding:12px}
.voice-left{left:28px}
.voice-right{left:445px}
.voice-photo{position:absolute;left:12px;top:12px;width:120px;height:148px;background:linear-gradient(160deg,#f3f3f3,#c8ccd0)}
.voice-table{position:absolute;left:142px;top:12px;width:246px;border-collapse:collapse;background:#fff;font-size:14px}
.voice-table th,.voice-table td{border:1px solid var(--line);padding:3px 8px;height:29.6px}
.voice-table th{width:96px;font-weight:500;text-align:left;background:#f5f5f5}
.voice-table td{font-weight:700}
.voice-text{position:absolute;left:12px;top:172px;width:376px;font-size:14px;line-height:1.85}
</style>
</head>
<body>
<div class="abs side-stripe"><span></span><span></span><span></span><span></span></div>
<div class="abs hiring-banner">Now Hiring!</div>
<div class="abs get-job">GET<br>JOB!!</div>

<div class="abs shop-mark"></div>
<h1 class="abs shop-name"><ruby>居酒屋まねき<rt>イザカヤマネキ</rt></ruby> <ruby>赤坂見附店<rt>アカサカミツケテン</rt></ruby></h1>
<div class="abs shop-rule"></div>

<div class="abs shop-photo" role="img" aria-label="店内で料理を持って笑顔で立つスタッフの写真"></div>
<div class="abs pr-box">
  <ruby>留学生<rt>りゅうがくせい</rt></ruby><ruby>大歓迎<rt>だいかんげい</rt></ruby>！<ruby>日本語<rt>にほんご</rt></ruby>があまり<ruby>喋<rt>しゃべ</rt></ruby>る
  ことができなくても、<ruby>日本語<rt>にほんご</rt></ruby>レベルに
  <ruby>合<rt>あ</rt></ruby>わせた<ruby>研修<rt>けんしゅう</rt></ruby>有り。<ruby>学校<rt>がっこう</rt></ruby>に<ruby>行<rt>い</rt></ruby>きなが
  らでも<ruby>無理<rt>むり</rt></ruby>なく<ruby>働<rt>はたら</rt></ruby>ける<ruby>早朝<rt>そうちょう</rt></ruby> 6:30〜
  <span class="accent">10:00のシフトも<ruby>可能<rt>かのう</rt></ruby>！</span>
</div>

<table class="abs info">
  <tr style="height:108px"><th><ruby>職種<rt>しょくしゅ</rt></ruby> / <ruby>賃金<rt>ちんぎん</rt></ruby><small>job/wage</small></th>
    <td>■<ruby>飲食接客<rt>いんしょくせっきゃく</rt></ruby>：¥1,000/h<br>■キッチン：¥980/h</td></tr>
  <tr style="height:52px"><th><ruby>勤務時間<rt>きんむじかん</rt></ruby><small>working hours</small></th>
    <td><ruby>平日土日<rt>へいじつどにち</rt></ruby> 6:30〜24:00</td></tr>
  <tr style="height:52px"><th><ruby>最寄駅<rt>もよりえき</rt></ruby><small>nearest station</small></th>
    <td><ruby>赤坂<rt>あかさか</rt></ruby>・<ruby>溜池山王<rt>ためいけさんのう</rt></ruby>・<ruby>赤坂見附<rt>あかさかみつけ</rt></ruby></td></tr>
</table>

<table class="abs qual">
  <tr><th rowspan="4"><ruby>応募条件<rt>おうぼじょうけん</rt></ruby><small>Qualifications</small></th>
    <td>■<ruby>飲食接客<rt>いんしょくせっきゃく</rt></ruby></td></tr>
  <tr><td class="sub">N3<ruby>以上<rt>いじょう</rt></ruby>(<ruby>応相談<rt>おうそうだん</rt></ruby>)</td></tr>
  <tr><td>■キッチン</td></tr>
  <tr><td class="sub">N4<ruby>以上<rt>いじょう</rt></ruby>(<ruby>応相談<rt>おうそうだん</rt></ruby>)</td></tr>
</table>

<div class="abs call">
  <div class="call-head">
    <svg width="26" height="26" viewBox="0 0 26 26" aria-hidden="true"><circle cx="13" cy="13" r="13" fill="var(--red)"/><path d="M9 7c1 0 2 3 2 4s-1 1-1 2 2 3 3 3 1-1 2-1 4 1 4 2-1 3-3 3c-4 0-9-5-9-10 0-2 1-3 2-3z" fill="#fff"/></svg>
    CALL US!
  </div>
  <div class="call-number">03-XXX-XXXX</div>
</div>
<div class="abs company">
  <ruby>株式会社<rt>かぶしきがいしゃ</rt></ruby> XXXXX <ruby>アルバイト採用係<rt>あるばいとさいようがかり</rt></ruby><br>
  <ruby>東京都港区<rt>とうきょうとみなとく</rt></ruby> XXXXXXXXXXXXXXX
</div>

<section class="abs voice voice-left">
  <div class="voice-photo" role="img" aria-label="先輩スタッフの写真"></div>
  <table class="voice-table">
    <tr><th>名前</th><td>ミンさん</td></tr>
    <tr><th>出身</th><td>ベトナム</td></tr>
    <tr><th>年齢</th><td>22才</td></tr>
    <tr><th>日本語レベル</th><td>N3</td></tr>
    <tr><th>在日期間</th><td>1年</td></tr>
  </table>
  <p class="voice-text"><ruby>最初<rt>さいしょ</rt></ruby>は<ruby>不安<rt>ふあん</rt></ruby>でしたが、<ruby>先輩<rt>せんぱい</rt></ruby>がやさしく<ruby>教<rt>おし</rt></ruby>えてくれたので<ruby>安心<rt>あんしん</rt></ruby>して<ruby>働<rt>はたら</rt></ruby>けます。<ruby>日本語<rt>にほんご</rt></ruby>も<ruby>上手<rt>じょうず</rt></ruby>になりました。<ruby>一緒<rt>いっしょ</rt></ruby>にがんばりましょう！</p>
</section>

<section class="abs voice voice-right">
  <div class="voice-photo" role="img" aria-label="先輩スタッフの写真"></div>
  <table class="voice-table">
    <tr><th>名前</th><td>リンさん</td></tr>
    <tr><th>出身</th><td>中国</td></tr>
    <tr><th>年齢</th><td>24才</td></tr>
    <tr><th>日本語レベル</th><td>N2</td></tr>
    <tr><th>在日期間</th><td>0.5年</td></tr>
  </table>
  <p class="voice-text"><ruby>学校<rt>がっこう</rt></ruby>の<ruby>予定<rt>よてい</rt></ruby>に<ruby>合<rt>あ</rt></ruby>わせてシフトを<ruby>決<rt>き</rt></ruby>められるので<ruby>便利<rt>べんり</rt></ruby>です。お<ruby>客<rt>きゃく</rt></ruby>さんとの<ruby>会話<rt>かいわ</rt></ruby>で<ruby>日本<rt>にほん</rt></ruby>の<ruby>文化<rt>ぶんか</rt></ruby>も<ruby>学<rt>まな</rt></ruby>べます。ぜひ<ruby>応募<rt>おうぼ</rt></ruby>してください！</p>
</section>
</body>
</html>
```